Warning Sign

I need a new security warning sign creating in a new theme. I have uploaded an old sign to give you an idea. However, the details are different.

The sign must be very large and very high definition. It will be printed at 600mm x 400mm
Telephone Number is 0800 514 3962
Website is www.kestrowline.co.uk
Email is security@kestrowline.co.uk

The company name is called "Velquor Security & Monitoring"

I have uploaded the new Logo, Letter Head and Business Card to give you an idea of the new theme.

List of Services is different to the old sign. They are as follows:

Static Security
Mobile Patrols
Alarm Response & Key Holding
Alarm & CCTV Monitoring
Welfare Hire

```html
<!DOCTYPE html>
<html lang="en">
<head>
<meta charset="utf-8">
<title>Velquor Security &amp; Monitoring – Warning Sign</title>
<link rel="stylesheet" href="https://fonts.googleapis.com/css2?family=Lato:wght@700;900&family=Barlow:wght@800&display=swap">
<style>
  :root {
    --brand-blue: #0a6fbd;
    --brand-blue-deep: #1d4fa3;
    --ink: #1b1b1d;
    --footer-black: #222325;
    --paper: #ffffff;
    --backdrop: #e7eaee;
    --illustration-a: #cfe0f4;
    --illustration-b: #8fb3e3;
  }
  * { margin: 0; padding: 0; box-sizing: border-box; }
  html, body { width: 1200px; height: 1120px; overflow: hidden; }
  body { background: var(--backdrop); font-family: "Lato", Arial, sans-serif; }

  .sign {
    position: absolute; left: 0; top: 160px;
    width: 1200px; height: 800px;
    background: var(--paper); overflow: hidden;
  }
  .sign-backdrop { position: absolute; inset: 0; }

  .sign-title {
    position: absolute; left: 680px; top: 38px;
    font-family: "Barlow", "Arial Black", sans-serif; font-weight: 800;
    font-size: 100px; letter-spacing: 2px; color: var(--paper); line-height: 1;
  }

  .brand {
    position: absolute; left: 70px; top: 290px;
    display: flex; align-items: center; gap: 18px;
  }
  .brand-dot { width: 54px; height: 54px; border-radius: 50%; background: var(--brand-blue); flex: none; }
  .brand-name {
    font-weight: 900; font-size: 40px; line-height: 1.1; color: var(--brand-blue);
  }

  .services {
    position: absolute; left: 70px; top: 440px; list-style: none;
  }
  .services li {
    display: flex; align-items: center; gap: 16px;
    font-weight: 700; font-size: 34px; line-height: 1; color: var(--ink);
    margin-bottom: 14px;
  }
  .services li::before {
    content: ""; width: 30px; height: 30px; border-radius: 50%;
    background: var(--brand-blue); flex: none;
  }

  .illustration {
    position: absolute; left: 640px; top: 400px; width: 500px; height: 270px;
    border-radius: 12px;
    background: radial-gradient(circle at 50% 45%, var(--illustration-b), var(--illustration-a) 70%);
  }

  .contact {
    position: absolute; left: 0; right: 0; top: 706px;
    text-align: center; color: var(--paper);
    font-weight: 700; font-size: 30px; line-height: 1.3;
  }
</style>
</head>
<body>
  <main class="sign">
    <svg class="sign-backdrop" width="1200" height="800" viewBox="0 0 1200 800" aria-hidden="true">
      <path d="M0 0 H1200 V380 C1080 370 950 325 800 260 C640 190 520 80 320 80 C170 80 50 160 0 300 Z" fill="var(--brand-blue)"/>
      <path d="M150 122 C210 75 260 52 320 52 C520 52 640 162 800 232 C950 297 1080 342 1200 352" fill="none" stroke="var(--paper)" stroke-width="8"/>
      <rect x="0" y="686" width="1200" height="8" fill="var(--brand-blue)"/>
      <rect x="0" y="694" width="1200" height="106" fill="var(--footer-black)"/>
    </svg>

    <h1 class="sign-title">WARNING</h1>

    <div class="brand">
      <span class="brand-dot"></span>
      <span class="brand-name">Velquor Security<br>&amp; Monitoring</span>
    </div>

    <ul class="services">
      <li>Static Security</li>
      <li>Mobile Patrols</li>
      <li>Alarm Response &amp; Key Holding</li>
      <li>Alarm &amp; CCTV Monitoring</li>
      <li>Welfare Hire</li>
    </ul>

    <div class="illustration" role="img" aria-label="Illustration of a shield with a tick surrounded by connected digital security icons: padlocks, devices, email, data storage and a login screen"></div>

    <p class="contact">Ph: 0800 514 3962 | www.kestrowline.co.uk<br>Email is security@kestrowline.co.uk</p>
  </main>
</body>
</html>
```